Marigold’s family restaurant & ice cream parlor

Looking for something that matches an old fashion vintage look for a family run business in an historic downtown district that is a unique nostalgic dining experience
With lots of memorabilia

Target Market(s)

Families

Industry/Entity Type

Diner , restaurant

Contact Information for Business Card

Picture of a Steam engine locomotive , ice cream cones, chalkboard look , black background

Font styles to use
Serif
Decorative

Colors

Designer to choose colors to be used in the design.

```html
<!DOCTYPE html>
<html lang="en">
<head>
<meta charset="utf-8">
<title>Marigold’s family restaurant &amp; ice cream parlor – business card</title>
<link rel="stylesheet" href="https://fonts.googleapis.com/css2?family=Federo&display=swap">
<style>
  :root {
    --backdrop: #e4e4e4;
    --card-black: #111111;
    --ink-deep: #050505;
    --silver: #c9c9c9;
    --silver-dim: #8f8f8f;
    --text-white: #f4f4f4;
  }
  * { margin: 0; padding: 0; box-sizing: border-box; }
  html, body {
    width: 1200px; height: 846px; overflow: hidden;
    background: var(--backdrop);
  }
  .sheet {
    position: relative; width: 1200px; height: 846px;
    display: flex; align-items: center; justify-content: center; gap: 40px;
  }
  .card {
    position: relative; width: 540px; height: 309px;
    background: var(--card-black); overflow: hidden;
    box-shadow: 0 6px 18px rgba(0,0,0,0.18);
    font-family: "Federo", sans-serif;
  }
  /* front face */
  .card-front .frame-outer,
  .card-front .frame-inner {
    position: absolute; border: 1px solid var(--silver-dim);
  }
  .card-front .frame-outer { inset: 14px; }
  .card-front .frame-inner { inset: 20px; border-color: var(--silver); }
  .brand {
    position: absolute; inset: 0;
    display: flex; flex-direction: column; align-items: center; justify-content: center;
    color: var(--silver); text-transform: uppercase; text-align: center;
  }
  .brand-kicker { font-size: 15px; letter-spacing: 3px; }
  .brand-meals { font-size: 11px; letter-spacing: 2px; margin-top: 8px; }
  .brand-row {
    display: flex; align-items: center; gap: 14px; margin: 4px 0 2px;
  }
  .brand-dot {
    width: 30px; height: 30px; border-radius: 50%;
    border: 2px solid var(--silver);
  }
  .brand-name { font-size: 56px; letter-spacing: 2px; line-height: 1.1; }
  .brand-parlor { font-size: 15px; letter-spacing: 3px; }
  .brand-est { font-size: 10px; letter-spacing: 2px; margin-top: 6px; }
  /* back face */
  .card-back { background: var(--ink-deep); }
  .engine-art {
    position: absolute; left: 0; top: 0; width: 540px; height: 309px;
  }
  .contact {
    position: absolute; right: 22px; top: 36px; width: 230px;
    color: var(--text-white); text-align: center;
  }
  .contact-name { font-size: 24px; margin-bottom: 22px; }
  .contact-line { font-size: 16px; line-height: 1.4; }
  .contact-address { margin-top: 18px; }
</style>
</head>
<body>
<main class="sheet">
  <section class="card card-front" aria-label="Business card front">
    <div class="frame-outer"></div>
    <div class="frame-inner"></div>
    <div class="brand">
      <p class="brand-kicker">Family Restaurant</p>
      <p class="brand-meals">Breakfast – Lunch – Dinner</p>
      <div class="brand-row">
        <span class="brand-dot"></span>
        <span class="brand-name">Marigold’s</span>
      </div>
      <p class="brand-parlor">Ice Cream Parlor</p>
      <p class="brand-est">Est. 1994</p>
    </div>
  </section>

  <section class="card card-back" aria-label="Business card back">
    <svg class="engine-art" viewBox="0 0 540 309" role="img"
         aria-label="Engraved illustration of a vintage steam locomotive with billowing smoke">
      <defs>
        <linearGradient id="engineTone" x1="0" y1="0" x2="0.3" y2="1">
          <stop offset="0" stop-color="#f2f2f2"/>
          <stop offset="0.35" stop-color="#bdbdbd"/>
          <stop offset="0.6" stop-color="#4a4a4a"/>
          <stop offset="1" stop-color="#1a1a1a"/>
        </linearGradient>
      </defs>
      <path d="M0 110 C40 90 90 70 150 60 C200 40 250 45 290 70 C310 90 330 110 340 150 C360 180 380 200 350 240 C330 270 310 300 300 309 L0 309 Z"
            fill="url(#engineTone)"/>
    </svg>
    <div class="contact">
      <p class="contact-name">Marigold Hale</p>
      <p class="contact-line">Tel. (555) 014 2790</p>
      <p class="contact-line">www.marigoldsdiner.com</p>
      <p class="contact-line contact-address">27 Elm Row Street,<br>Cedarbrook, Ohio 45012,<br>United States</p>
    </div>
  </section>
</main>
</body>
</html>
```